Fernvale Craft Works business card design- Fine Art sculpture business (Contract guaranteed)

This business card is for a fine art business. Though we don't have a website up and running yet it should be up soon. I would like the business card to be elegant and fairly simple with a picture of one of my sculptures on the front (you might need to photoshop out the background) as well as my basic contact info (my name,phone # and e-mail). On the back I'd like it to be pretty simple with just "Notes" and some blank lines for writing in info.

Target Market(s)

High end artwork buyers

Industry/Entity Type

Art Gallery

Contact Information for Business Card

Marlo Prewitt Phone: (555) 213-4098 E-mail: marlo@quillbrookmail.com Facebook: @fernvalecraftworks Instagram: fernvalecraftworks

Colors

Designer to choose colors to be used in the design.

Requirements
Must have
• *A picture of one of my sculptures*, my name, business name (Fernvale Craft Works), e-mail, phone #, and a notes section on the back.
• Fernvale Craft Works
• Marlo Prewitt
• (555)213-4098
• marlo@quillbrookmail.com
• Facebook: @fernvalecraftworks
• Instagram: fernvalecraftworks
Nice to have
• It'd be nice if you can crop out the background in the sculpture pictures, which ever one you end up using.

```html
<!DOCTYPE html>
<html lang="en">
<head>
<meta charset="utf-8">
<title>Fernvale Craft Works – Business Card</title>
<link rel="stylesheet" href="https://fonts.googleapis.com/css2?family=Alfa+Slab+One&family=Questrial&display=swap">
<style>
  :root {
    --card-grey: #959694;
    --page-white: #ffffff;
    --ink-black: #111111;
    --name-white: #ffffff;
    --fold-shadow: rgba(0, 0, 0, 0.35);
    --amethyst-deep: #4a2f9a;
    --amethyst-light: #8a72c8;
    --granite: #6b6d6c;
  }
  * { margin: 0; padding: 0; box-sizing: border-box; }
  html, body {
    width: 1200px; height: 800px; overflow: hidden;
    background: var(--page-white);
  }
  .canvas { position: relative; width: 1200px; height: 800px; }

  /* Back side: notes */
  .card-back {
    position: absolute; left: 132px; top: 12px;
    width: 970px; height: 370px;
    background: var(--card-grey);
    overflow: hidden;
  }
  .card-back__spine {
    position: absolute; left: 0; top: 0;
    width: 170px; height: 100%;
    background: var(--card-grey);
    box-shadow: 4px 0 10px var(--fold-shadow);
    border-right: 1px solid rgba(0,0,0,0.15);
  }
  .notes-title {
    position: absolute; left: 310px; top: 20px;
    font-family: "Questrial", sans-serif;
    font-weight: 400;
    font-size: 60px; line-height: 1;
    color: var(--ink-black);
    text-decoration: underline;
    text-decoration-thickness: 2px;
    text-underline-offset: 3px;
  }
  .notes-lines { position: absolute; left: 0; top: 0; }

  /* Front side */
  .card-front {
    position: absolute; left: 132px; top: 404px;
    width: 972px; height: 334px;
    background: var(--card-grey);
  }
  .sculpture-photo {
    position: absolute; left: 78px; top: 8px;
    width: 182px; height: 320px;
    background: linear-gradient(180deg, var(--amethyst-light) 0%, var(--amethyst-deep) 70%, var(--granite) 100%);
  }
  .owner-name {
    position: absolute; left: 362px; top: 60px;
    font-family: "Alfa Slab One", serif;
    font-style: italic;
    font-weight: 400;
    font-size: 40px; line-height: 1;
    letter-spacing: 3px;
    color: var(--name-white);
  }
  .studio-name {
    position: absolute; left: 364px; top: 97px;
    font-family: "Questrial", sans-serif;
    font-size: 31px; line-height: 1;
    color: var(--ink-black);
  }
  .contact-band {
    position: absolute; left: 132px; top: 744px;
    width: 972px; height: 34px;
    background: var(--card-grey);
    font-family: "Questrial", sans-serif;
    font-size: 28px; line-height: 34px;
    color: var(--name-white);
    letter-spacing: 0.5px;
  }
  .contact-band__email { position: absolute; left: 16px; top: 0; }
  .contact-band__phone { position: absolute; left: 602px; top: 0; letter-spacing: 4px; }
</style>
</head>
<body>
<main class="canvas">

  <section class="card-back" aria-label="Card back – notes">
    <div class="card-back__spine"></div>
    <h2 class="notes-title">Notes</h2>
    <svg class="notes-lines" width="970" height="370" viewBox="0 0 970 370" aria-hidden="true">
      <g fill="none" stroke="var(--ink-black)" stroke-width="3">
        <ellipse cx="220" cy="104" rx="14" ry="11"/>
        <ellipse cx="220" cy="151" rx="14" ry="11"/>
        <ellipse cx="220" cy="200" rx="14" ry="11"/>
        <ellipse cx="220" cy="254" rx="14" ry="11"/>
        <ellipse cx="220" cy="310" rx="14" ry="11"/>
      </g>
      <g stroke="var(--ink-black)" stroke-width="4" stroke-linecap="round" stroke-dasharray="0 8">
        <line x1="276" y1="112" x2="806" y2="112"/>
        <line x1="276" y1="162" x2="806" y2="162"/>
        <line x1="276" y1="214" x2="806" y2="214"/>
        <line x1="276" y1="266" x2="806" y2="266"/>
        <line x1="276" y1="318" x2="806" y2="318"/>
      </g>
    </svg>
  </section>

  <section class="card-front" aria-label="Card front">
    <div class="sculpture-photo" role="img" aria-label="Photograph of an amethyst geode sculpture on a granite base"></div>
    <h1 class="owner-name">MARLO PREWITT</h1>
    <p class="studio-name">Fernvale Craft Works</p>
  </section>

  <footer class="contact-band">
    <span class="contact-band__email">marlo@quillbrookmail.com</span>
    <span class="contact-band__phone">+555 213-4098</span>
  </footer>

</main>
</body>
</html>
```